Digital content business needs banner ads

We sell content - if you need an article to put on your website or in a newsletter, you can purchase a ready made article from us and edit it to your liking to use straight away. This could be any kind of article, but this banner ad will be aimed at real estate agents. You can see the website (and the style of articles) here https://www.thebluelanternpost.com.au
The banner is meant to solve the problem of the front desk admin or agent trying to think of something to write to put in their email newsletter. This will save them time as they can just select an article from our library and use it (for a fee of course!).
Needs to have the words:
--------------------------------------------------
Find the next article for your newsletter
---------------------------------------------------
Some imagery would be good rather than plain text.
With a call to action like click here button or similar
Required sizes (or provide a set of standard sized ads):
728 x 90
970 x 250
300x250
Real Estate Agents

```html
<!DOCTYPE html>
<html lang="en">
<head>
<meta charset="utf-8">
<title>The Blue Lantern Post – Banner Set</title>
<link href="https://fonts.googleapis.com/css2?family=Poppins:wght@400;600;700&display=swap" rel="stylesheet">
<style>
  :root{
    --backdrop:#595959;
    --navy:#27487c;
    --paper:#e8e8e8;
    --green:#3ba343;
    --white:#ffffff;
    --photo-light:#e9e6e2;
    --photo-mid:#c9bfb6;
    --photo-warm:#b0706a;
  }
  html,body{margin:0;padding:0;width:1200px;height:908px;overflow:hidden;background:var(--backdrop);}
  .stage{position:absolute;left:0;top:0;width:1311px;height:992px;transform:scale(0.91533);transform-origin:0 0;font-family:'Poppins',sans-serif;}
  .banner{position:absolute;overflow:hidden;background:var(--paper);}
  .banner svg.shapes{position:absolute;left:0;top:0;}
  .photo{position:absolute;background:linear-gradient(115deg,var(--photo-light) 0%,var(--photo-mid) 45%,var(--photo-warm) 65%,var(--photo-light) 100%);}
  .headline{position:absolute;margin:0;color:var(--white);font-weight:400;line-height:1.04;}
  .headline strong{font-weight:700;}
  .cta{position:absolute;display:flex;align-items:center;justify-content:center;background:var(--green);color:var(--white);font-weight:600;border-radius:999px;letter-spacing:.04em;text-decoration:none;}
  .brand{position:absolute;display:flex;align-items:center;gap:8px;color:var(--navy);font-weight:700;line-height:1.05;}
  .brand-square{flex:none;background:var(--navy);}

  /* 970 x 250 */
  .banner-billboard{left:177px;top:169px;width:970px;height:250px;}
  .banner-billboard .photo{left:0;top:0;width:460px;height:250px;}
  .banner-billboard .headline{left:422px;top:64px;font-size:36px;}
  .banner-billboard .cta{left:467px;top:159px;width:245px;height:46px;font-size:20px;}
  .banner-billboard .brand{left:838px;top:100px;font-size:19px;}
  .banner-billboard .brand-square{width:22px;height:22px;}

  /* 728 x 90 */
  .banner-leaderboard{left:177px;top:445px;width:728px;height:90px;}
  .banner-leaderboard .photo{left:540px;top:0;width:188px;height:90px;}
  .banner-leaderboard .headline{left:173px;top:22px;font-size:21px;}
  .banner-leaderboard .cta{left:391px;top:31px;width:147px;height:31px;font-size:13px;}
  .banner-leaderboard .brand{left:30px;top:27px;font-size:14px;gap:6px;}
  .banner-leaderboard .brand-square{width:16px;height:16px;}

  /* 300 x 250 */
  .banner-rectangle{left:177px;top:572px;width:300px;height:250px;}
  .banner-rectangle .photo{left:0;top:0;width:300px;height:190px;}
  .banner-rectangle .headline{left:16px;top:41px;font-size:19px;line-height:1.18;}
  .banner-rectangle .cta{left:135px;top:205px;width:147px;height:31px;font-size:13px;}
  .banner-rectangle .brand{left:34px;top:202px;font-size:12px;gap:6px;}
  .banner-rectangle .brand-square{width:14px;height:14px;}
</style>
</head>
<body>
<div class="stage">

  <section class="banner banner-billboard" aria-label="970 by 250 banner">
    <div class="photo" role="img" aria-label="Photo of a frustrated agent at a desk with a laptop and crumpled paper"></div>
    <svg class="shapes" width="970" height="250" viewBox="0 0 970 250" aria-hidden="true">
      <polygon fill="#ffffff" points="404,0 830,0 812,40 818,60 806,100 812,125 800,165 806,190 792,225 786,250 318,250 330,215 340,200 348,160 362,140 368,105 380,85 386,50 398,30"/>
      <polygon fill="#27487c" points="410,0 822,0 806,40 811,60 799,100 805,125 793,165 799,190 786,225 779,250 326,250 337,215 347,200 355,160 369,140 375,105 387,85 393,50 404,30"/>
    </svg>
    <h2 class="headline">Find the <strong>next article</strong><br>for your <strong>newsletter</strong></h2>
    <a class="cta" href="https://www.thebluelanternpost.com.au">CLICK HERE</a>
    <div class="brand"><span class="brand-square"></span><span>The Blue<br>Lantern Post</span></div>
  </section>

  <section class="banner banner-leaderboard" aria-label="728 by 90 banner">
    <div class="photo" role="img" aria-label="Photo of a frustrated agent at a desk with a laptop"></div>
    <svg class="shapes" width="728" height="90" viewBox="0 0 728 90" aria-hidden="true">
      <polygon fill="#ffffff" points="150,0 578,0 570,20 574,35 562,55 565,70 552,90 136,90 142,70 140,50 146,30 144,15"/>
      <polygon fill="#27487c" points="155,0 572,0 564,20 568,35 556,55 559,70 546,90 141,90 147,70 145,50 151,30 149,15"/>
    </svg>
    <div class="brand"><span class="brand-square"></span><span>The Blue<br>Lantern Post</span></div>
    <h2 class="headline">Find the <strong>next article</strong><br>for your <strong>newsletter</strong></h2>
    <a class="cta" href="https://www.thebluelanternpost.com.au">CLICK HERE</a>
  </section>

  <section class="banner banner-rectangle" aria-label="300 by 250 banner">
    <div class="photo" role="img" aria-label="Photo of a frustrated agent at a desk with crumpled paper"></div>
    <svg class="shapes" width="300" height="250" viewBox="0 0 300 250" aria-hidden="true">
      <path fill="#27487c" d="M0,0 H126 C160,40 160,140 118,178 L0,178 Z"/>
      <polygon fill="#ffffff" points="0,176 30,180 60,172 95,182 130,174 165,180 200,170 235,178 270,172 300,176 300,188 0,188"/>
      <polygon fill="#e8e8e8" points="0,184 35,188 70,181 105,190 140,183 175,189 210,180 245,187 280,181 300,184 300,250 0,250"/>
    </svg>
    <h2 class="headline">Find the<br><strong>next article</strong><br>for your<br><strong>newsletter</strong></h2>
    <div class="brand"><span class="brand-square"></span><span>The Blue<br>Lantern Post</span></div>
    <a class="cta" href="https://www.thebluelanternpost.com.au">CLICK HERE</a>
  </section>

</div>
</body>
</html>
```